Etiketten-Design für Kräuterlikör
Zielgruppe
Firma: Spirituosen Großhandel
Zielgruppe: Nightclub Junge
Aufgabenstellung
Produkt: Kräuterlikör 30%, 0,7L
Marke: Sternfels/Flink/Rost und Reif
Format: 110mm* 68mm x2 + 34mm * 112mm x1
Seite: Vor-, Hals- und Rückseite (3 Seite)
Ursprung: Deutschland
Art: klassisch oder modern, Aber hochwertig
Flasch: Dunkelgrün
Hochwertig wegen Primium Qualität
Flasche und Etikett passen miteinander

```html
<!DOCTYPE html>
<html lang="de">
<head>
<meta charset="utf-8">
<title>Forstglut Kräuterlikör – Frontetikett</title>
<link rel="stylesheet" href="https://fonts.googleapis.com/css2?family=Almendra:wght@400;700&family=Libre+Baskerville:wght@700&family=Oswald:wght@300&display=swap">
<style>
  :root {
    --stage: #d9d9d9;
    --frame: #ffffff;
    --label-dark: #1c1b1d;
    --label-mid: #4a4649;
    --label-glow: #8d8a8c;
    --badge: #232226;
    --ink-light: #f4f2ee;
    --gold: #d9a646;
    --gold-soft: rgba(217, 166, 70, 0.35);
    --ornament-soft: rgba(244, 242, 238, 0.18);
  }
  * { margin: 0; padding: 0; box-sizing: border-box; }
  html, body {
    width: 1200px;
    height: 887px;
    overflow: hidden;
    background: var(--stage);
  }
  .canvas {
    position: relative;
    width: 1200px;
    height: 887px;
    display: flex;
    align-items: center;
    justify-content: center;
  }
  .front-label {
    position: relative;
    width: 493px;
    height: 800px;
    background: var(--frame);
    padding: 17px;
  }
  .label-field {
    position: relative;
    width: 100%;
    height: 100%;
    overflow: hidden;
    background: var(--label-dark);
  }
  .label-texture {
    position: absolute;
    inset: 0;
    background:
      radial-gradient(ellipse 62% 48% at 50% 40%, var(--label-glow) 0%, var(--label-mid) 45%, transparent 80%),
      linear-gradient(180deg, var(--label-mid) 0%, var(--label-dark) 30%, #2b292b 70%, var(--label-dark) 100%);
  }
  .badge {
    position: absolute;
    left: 29px;
    top: 123px;
    width: 400px;
    height: 400px;
    border-radius: 50%;
    background: radial-gradient(circle at 50% 45%, #2e2d31 0%, var(--badge) 70%);
    box-shadow: 0 0 40px rgba(200, 198, 200, 0.35);
  }
  .mark-placeholder {
    position: absolute;
    left: 93px;
    top: 58px;
    width: 227px;
    height: 174px;
    background: radial-gradient(ellipse at 50% 60%, var(--gold-soft) 0%, transparent 70%);
  }
  .ornament {
    position: absolute;
    background: var(--ornament-soft);
    border-radius: 6px;
  }
  .ornament-left  { left: 104px; top: 190px; width: 70px; height: 56px; }
  .ornament-right { left: 287px; top: 190px; width: 70px; height: 56px; }
  .ornament-rule  { left: 167px; top: 451px; width: 150px; height: 22px; }
  .brand-name {
    position: absolute;
    top: 254px;
    left: 0;
    right: 0;
    text-align: center;
    font-family: "Almendra", serif;
    font-weight: 700;
    font-size: 86px;
    line-height: 1;
    color: var(--ink-light);
  }
  .product-type {
    position: absolute;
    top: 370px;
    left: 0;
    right: 0;
    text-align: center;
    font-family: "Almendra", serif;
    font-weight: 400;
    font-size: 36px;
    line-height: 1;
    color: var(--gold);
  }
  .tagline {
    position: absolute;
    top: 548px;
    left: 0;
    right: 0;
    text-align: center;
    font-family: "Libre Baskerville", serif;
    font-weight: 700;
    font-size: 14.5px;
    line-height: 26px;
    letter-spacing: 0.06em;
    color: var(--ink-light);
  }
  .facts {
    position: absolute;
    top: 684px;
    left: 40px;
    right: 43px;
    display: flex;
    justify-content: space-between;
    font-family: "Oswald", sans-serif;
    font-weight: 300;
    font-size: 37px;
    line-height: 1;
    color: var(--ink-light);
  }
</style>
</head>
<body>
  <main class="canvas">
    <section class="front-label">
      <div class="label-field">
        <div class="label-texture" role="img" aria-label="Dunkles Karomuster in Grau- und Schwarztönen mit hellem Lichtschein zur Mitte"></div>
        <div class="badge"></div>
        <div class="mark-placeholder" role="img" aria-label="Platz für das goldene Markenzeichen über dem Siegel"></div>
        <div class="ornament ornament-left" role="img" aria-label="Feines Zweigornament links"></div>
        <div class="ornament ornament-right" role="img" aria-label="Feines Zweigornament rechts"></div>
        <div class="ornament ornament-rule" role="img" aria-label="Verziertes Zweigornament unter der Produktbezeichnung"></div>
        <h1 class="brand-name">Forstglut</h1>
        <p class="product-type">Kräuterlikör</p>
        <p class="tagline">Qualitätströpfchen<br>nach einem alten Hausrezept</p>
        <div class="facts">
          <span class="volume">0,7 l</span>
          <span class="strength">30% vol</span>
        </div>
      </div>
    </section>
  </main>
</body>
</html>
```